Small but growing painting company. Have built up a steady client base. Want to start having a more professional look. Want to start with changing my business cards, and also getting new logo and tee shirts.

Target Market(s)

Home owners, property management companies, all ages 30-70

Industry/Entity Type

Painting And Decorating

Contact Information for Business Card

Bright Ridge Painting LLC Mark Delvecchi 630-584-3907 interior, exterior, vaulted ceiling, drywall repair, pressure washing, kitchen cabinets, epoxy, garage floors,

Font styles to use
Sans Serif
Other font styles liked:
• Harrington

Colors
0355a3
ffffff
ec1f27
000000
3176b5
0493ce
474747
b7b7b7

Requirements
Must have
• Creative, something that doesn’t look like every other painting card.
Nice to have
• I would like something with an arrow or something going to a point

```html
<!DOCTYPE html>
<html lang="en">
<head>
<meta charset="utf-8">
<title>Bright Ridge Painting LLC – Business Card</title>
<link rel="stylesheet" href="https://fonts.googleapis.com/css2?family=Open+Sans:wght@400;700&display=swap">
<style>
  :root {
    --brand-blue: #0355a3;
    --charcoal: #474747;
    --white: #ffffff;
    --pattern-light: #f6f6f6;
    --pattern-mid: #ececec;
  }
  html, body {
    margin: 0;
    padding: 0;
    width: 1200px;
    height: 800px;
    overflow: hidden;
    background: var(--white);
  }
  .card {
    position: relative;
    width: 1200px;
    height: 800px;
    overflow: hidden;
    background: var(--white);
    font-family: "Open Sans", Verdana, sans-serif;
  }
  .card-shapes {
    position: absolute;
    inset: 0;
    width: 1200px;
    height: 800px;
  }
  .backdrop-texture { fill: url(#pattern-tone); }
  .accent-stripe, .services-band { fill: var(--brand-blue); }
  .charcoal-panel { fill: var(--charcoal); }
  .contact-icon { fill: var(--white); }

  .brand-name {
    position: absolute;
    left: 40px;
    top: 214px;
    width: 440px;
    margin: 0;
    font-size: 56px;
    font-weight: 700;
    line-height: 1.08;
    color: var(--charcoal);
  }
  .contact-name,
  .contact-phone {
    position: absolute;
    margin: 0;
    color: var(--white);
    font-weight: 400;
    line-height: 1;
  }
  .contact-name {
    left: 733px;
    top: 350px;
    font-size: 44px;
  }
  .contact-phone {
    left: 640px;
    top: 522px;
    font-size: 52px;
    letter-spacing: 1px;
  }
  .services {
    position: absolute;
    left: 0;
    top: 694px;
    width: 1200px;
    margin: 0;
    text-align: center;
    color: var(--white);
    font-size: 33px;
    line-height: 48px;
    white-space: nowrap;
  }
</style>
</head>
<body>
  <main class="card">
    <svg class="card-shapes" viewBox="0 0 900 600" width="1200" height="800">
      <defs>
        <linearGradient id="pattern-tone" x1="0" y1="0" x2="1" y2="1">
          <stop offset="0" stop-color="#ececec"/>
          <stop offset="0.55" stop-color="#f6f6f6"/>
          <stop offset="1" stop-color="#ffffff"/>
        </linearGradient>
      </defs>

      <rect class="backdrop-texture" x="0" y="0" width="650" height="520" role="img" aria-label="Faint light grey honeycomb texture across the background"/>

      <polygon class="accent-stripe" points="445,185 528,185 610,520 240,520"/>

      <polygon class="charcoal-panel"
        points="640,0 900,0 900,520 325,520 372,443 429,443 465,383 408,383 450,313 501,313 537,253 487,253"/>

      <rect class="services-band" x="0" y="520" width="900" height="80"/>

      <g class="contact-icon icon-person">
        <circle cx="491" cy="277" r="5.5"/>
        <path d="M481 294 a10 9 0 0 1 20 0 z"/>
      </g>

      <g class="contact-icon icon-phone">
        <path d="M414 399 l5 -2 l4 8 l-3 3 c1 4 3 8 6 11 l3 -2 l6 6 l-3 4 c-9 -2 -18 -16 -18 -28 z"/>
      </g>
    </svg>

    <h1 class="brand-name">Bright Ridge<br>Painting LLC</h1>

    <p class="contact-name">Mark Delvecchi</p>
    <p class="contact-phone">630-584-3907</p>

    <p class="services">Interior | Exterior | Vaulted ceiling | Drywall repair | Pressure washing<br>Kitchen cabinets | Epoxy | Garage floors</p>
  </main>
</body>
</html>
```